Used Car Dealer seeks an Amazing Business Card Design

We are looking for a business card design that incorporates our logo and grabs the attention of anyone we give the business card to.

Looking to use the same colors as the logo. Our Logo choice is the black background with Red and Silver/Grey Lettering.

We also would like to see some embossed designs.

Target Market(s)

Used Car Buyers, Automotive, Auto

Industry/Entity Type

Automotive

Contact Information for Business Card

BVEX7K
Gordon Whitley
482 Tenbrook Lane
Suite 305
Roswell, GA 30098
Office (770) 555-0142
Cell (770) 555-0187
bvex7kga@mailnest.example
www.bvex7kga.example

Colors
ffffff
ee3036

Requirements
Must have
• Must include our logo (Black Background with Red and Silver/Grey Lettering)
Nice to have
• Embossed Design. Can be Single or Double Sided.

```html
<!DOCTYPE html>
<html lang="en">
<head>
<meta charset="utf-8">
<title>BVEX7K Business Card</title>
<link href="https://fonts.googleapis.com/css2?family=Open+Sans:wght@400;600;700&display=swap" rel="stylesheet">
<style>
  :root {
    --page-bg: #3a3a3a;
    --card-black: #050505;
    --card-black-soft: #1c1c1c;
    --brand-red: #ee3036;
    --red-deep: #b00008;
    --red-dark: #8a0006;
    --silver-light: #f2f2f2;
    --silver-mid: #b9b9b9;
    --silver-dark: #7d7d7d;
    --ink: #111111;
    --white: #ffffff;
  }
  * { margin: 0; padding: 0; box-sizing: border-box; }
  html, body {
    width: 1200px; height: 750px; overflow: hidden;
    background: var(--page-bg);
    font-family: "Open Sans", Arial, sans-serif;
  }
  .canvas { position: relative; width: 1200px; height: 750px; }
  .card {
    position: absolute; top: 228px;
    width: 461px; height: 262px;
    border-radius: 12px; overflow: hidden;
  }
  .card-front { left: 124px; background: var(--card-black); }
  .card-back {
    left: 618px;
    background: radial-gradient(ellipse at 50% 45%, var(--silver-light) 0%, var(--silver-mid) 55%, var(--silver-dark) 100%);
  }
  .front-bands { position: absolute; inset: 0; }
  .brand-name {
    position: absolute; left: 240px; top: 68px;
    font-size: 34px; font-weight: 700; letter-spacing: 1px;
    color: var(--white);
  }
  .holder-name {
    position: absolute; left: 23px; top: 155px;
    font-size: 16px; font-weight: 600; color: var(--ink);
    text-transform: uppercase;
  }
  .divider {
    position: absolute; left: 23px; top: 184px; width: 396px; height: 1px;
    background: rgba(0,0,0,0.55);
  }
  .contact-list {
    position: absolute; left: 23px; top: 194px; list-style: none;
    font-size: 12px; color: var(--ink); line-height: 18px;
  }
  .contact-list li { display: flex; align-items: center; gap: 6px; }
  .contact-list svg { width: 11px; height: 11px; fill: var(--ink); }
  .address {
    position: absolute; right: 28px; top: 196px; text-align: right;
    font-size: 12px; color: var(--ink); line-height: 16.5px; font-style: normal;
  }
  .website {
    position: absolute; left: 0; right: 0; top: 146px; text-align: center;
    font-size: 19px; font-weight: 700; color: var(--ink); letter-spacing: 0.5px;
    text-transform: uppercase;
  }
</style>
</head>
<body>
<div class="canvas">

  <section class="card card-front">
    <svg class="front-bands" viewBox="0 0 461 262" preserveAspectRatio="none" aria-hidden="true">
      <defs>
        <radialGradient id="blackGlow" cx="62%" cy="75%" r="60%">
          <stop offset="0" stop-color="var(--card-black-soft)"/>
          <stop offset="1" stop-color="var(--card-black)"/>
        </radialGradient>
        <linearGradient id="silverBand" x1="0" x2="1" y1="0" y2="0">
          <stop offset="0" stop-color="var(--silver-dark)"/>
          <stop offset="0.5" stop-color="var(--silver-light)"/>
          <stop offset="1" stop-color="var(--silver-dark)"/>
        </linearGradient>
        <radialGradient id="redGlow" cx="60%" cy="50%" r="65%">
          <stop offset="0" stop-color="var(--brand-red)"/>
          <stop offset="0.6" stop-color="var(--red-deep)"/>
          <stop offset="1" stop-color="var(--red-dark)"/>
        </radialGradient>
      </defs>
      <rect width="461" height="262" fill="url(#blackGlow)"/>
      <polygon points="196,142 461,142 461,157 210,157" fill="url(#silverBand)"/>
      <polygon points="0,142 196,142 212,158 461,158 461,262 0,262" fill="url(#redGlow)"/>
    </svg>
    <div class="brand-name">BVEX7K</div>
    <h1 class="holder-name">Gordon Whitley</h1>
    <div class="divider"></div>
    <ul class="contact-list">
      <li><svg viewBox="0 0 24 24"><path d="M6.6 10.8a15.1 15.1 0 0 0 6.6 6.6l2.2-2.2a1 1 0 0 1 1-.25 11.4 11.4 0 0 0 3.6.57 1 1 0 0 1 1 1V20a1 1 0 0 1-1 1A17 17 0 0 1 3 4a1 1 0 0 1 1-1h3.5a1 1 0 0 1 1 1c0 1.25.2 2.45.57 3.57a1 1 0 0 1-.25 1z"/></svg>(770) 555-0142</li>
      <li><svg viewBox="0 0 24 24"><path d="M7 1h10a2 2 0 0 1 2 2v18a2 2 0 0 1-2 2H7a2 2 0 0 1-2-2V3a2 2 0 0 1 2-2zm0 3v14h10V4zm5 15.5a1.2 1.2 0 1 0 0 2.4 1.2 1.2 0 0 0 0-2.4z"/></svg>(770) 555-0187</li>
      <li><svg viewBox="0 0 24 24"><path d="M2 5h20v14H2zm2 2v.5l8 5 8-5V7z"/></svg>bvex7kga@mailnest.example</li>
    </ul>
    <address class="address">
      482 Tenbrook Lane<br>
      Suite 305<br>
      Roswell, GA 30098
    </address>
  </section>

  <section class="card card-back">
    <div class="website">www.bvex7kga.example</div>
  </section>

</div>
</body>
</html>
```